IT Services, Internet & Telephone Brochure

We need a new brochure that captures our core services. We have attached a pdf made in powerpoint providing the majority of content we would like. We have also included our telephone brochure as a example of colors and design that we liked. Lastly, we would like the designer to take liberty in developing a clean, professional but eye catching design.

```html
<!DOCTYPE html>
<html lang="en">
<head>
<meta charset="utf-8">
<title>Norvane – Phone Services Flyer</title>
<link rel="stylesheet" href="https://fonts.googleapis.com/css2?family=Raleway:wght@300;400;500;600;700;800&family=Roboto+Condensed:wght@400&display=swap">
<style>
  :root {
    --royal: #1212b0;
    --royal-deep: #0a0f8a;
    --navy: #0d1430;
    --night: #0a0d18;
    --orange: #ff8a00;
    --orange-light: #ffa21a;
    --ink: #121838;
    --grey: #6b7078;
    --white: #ffffff;
    --stage: #eef0f4;
  }
  * { margin: 0; padding: 0; box-sizing: border-box; }
  html, body { width: 1200px; height: 1200px; overflow: hidden; background: var(--stage); }
  body { position: relative; font-family: "Raleway", sans-serif; color: var(--ink); }

  .flyer {
    position: absolute; left: 169px; top: 0;
    width: 963px; height: 1340px;
    transform: scale(0.8955); transform-origin: top left;
    background: var(--white); overflow: hidden;
  }
  .flyer-shapes { position: absolute; inset: 0; }
  .abs { position: absolute; }

  .brand-box { left: 79px; top: 0; width: 383px; height: 240px; display: flex; flex-direction: column; align-items: center; justify-content: center; padding-top: 20px; }
  .brand-name { font-weight: 800; font-size: 92px; line-height: 1; color: var(--royal); letter-spacing: -2px; }
  .brand-tagline { font-family: "Roboto Condensed", sans-serif; font-size: 15px; color: var(--grey); margin-top: 6px; }

  .contact { left: 702px; top: 66px; list-style: none; color: var(--white); font-size: 17px; }
  .contact li { display: flex; align-items: center; height: 33px; }
  .contact svg { width: 20px; height: 20px; margin-right: 14px; }

  .hero { left: 79px; width: 383px; text-align: center; color: var(--white); }
  .hero-phone { top: 352px; font-weight: 700; font-size: 74px; letter-spacing: 8px; line-height: 1; }
  .hero-services { top: 428px; font-weight: 300; font-size: 56px; letter-spacing: 4px; line-height: 1; }
  .hero-price { top: 502px; font-weight: 800; font-size: 66px; line-height: 1; }
  .hero-period { top: 584px; font-weight: 300; font-size: 22px; letter-spacing: 3px; }
  .hero-icon { left: 230px; top: 638px; width: 82px; height: 80px; }

  .fiber-title { left: 150px; top: 822px; font-weight: 800; font-size: 31px; line-height: 1.22; letter-spacing: 2.5px; color: var(--royal); }
  .sub-head { font-weight: 500; font-size: 16.5px; color: var(--ink); }
  .bullets { list-style: none; font-size: 13px; }
  .bullets li { position: relative; padding-left: 22px; }
  .bullets li::before { content: ""; position: absolute; left: 0; top: 6px; width: 7px; height: 7px; border-radius: 50%; background: var(--ink); }
  .bandwidth-head { left: 150px; top: 911px; }
  .bandwidth-list { left: 150px; top: 945px; }
  .bandwidth-list li { height: 21px; }
  .fiber-notes { left: 150px; top: 1033px; width: 310px; font-size: 12.5px; line-height: 1.25; }

  .column-rule { left: 473px; top: 775px; width: 2px; height: 322px; background: var(--royal); }
  .phone-col { left: 499px; width: 380px; }
  .phone-col .bullets { padding-left: 16px; }
  .phone-col .bullets li { padding-left: 22px; line-height: 1.2; margin-bottom: 8px; }
  .opts-head { top: 776px; }
  .opts-list { top: 808px; }
  .pricing-head { top: 916px; }
  .pricing-list { top: 948px; }
  .pricing-list li { margin-bottom: 12px !important; }
  .features-head { top: 1023px; }
  .features-text { top: 1052px; padding-left: 16px; font-size: 12.5px; line-height: 1.25; }

  .services-title { left: 65px; top: 1162px; font-size: 21px; font-weight: 400; color: var(--white); }
  .service-list { list-style: none; color: var(--white); font-size: 13px; }
  .service-list li { position: relative; padding-left: 23px; height: 19px; }
  .service-list li::before { content: ""; position: absolute; left: 3px; top: 5px; width: 7px; height: 7px; border-radius: 50%; background: var(--white); }
  .svc-1 { left: 67px; top: 1203px; }
  .svc-2 { left: 364px; top: 1203px; }
  .svc-3 { left: 667px; top: 1203px; }
  .rate-note { left: 0; width: 963px; top: 1300px; text-align: center; color: var(--white); font-size: 12.5px; }
</style>
</head>
<body>
<main class="flyer">
  <svg class="flyer-shapes" viewBox="0 0 963 1340" width="963" height="1340">
    <defs>
      <linearGradient id="night-sky" x1="0" y1="0" x2="1" y2="1">
        <stop offset="0" stop-color="#1a2350"/>
        <stop offset="0.45" stop-color="#0b0f1c"/>
        <stop offset="1" stop-color="#1c2a4a"/>
      </linearGradient>
      <radialGradient id="city-glow" cx="0.72" cy="0.62" r="0.45">
        <stop offset="0" stop-color="#6a5430" stop-opacity="0.7"/>
        <stop offset="1" stop-color="#0b0f1c" stop-opacity="0"/>
      </radialGradient>
      <linearGradient id="footer-band" x1="0" y1="0" x2="1" y2="0">
        <stop offset="0" stop-color="#1010b8"/>
        <stop offset="0.55" stop-color="#101a5a"/>
        <stop offset="1" stop-color="#0c1226"/>
      </linearGradient>
      <linearGradient id="blue-bar" x1="0" y1="0" x2="1" y2="0">
        <stop offset="0" stop-color="#1a5fc8"/>
        <stop offset="1" stop-color="#1212a0"/>
      </linearGradient>
      <linearGradient id="orange-bar" x1="0" y1="0" x2="1" y2="0">
        <stop offset="0" stop-color="#ff9a10"/>
        <stop offset="1" stop-color="#ff7a00"/>
      </linearGradient>
    </defs>

    <g role="img" aria-label="Photo: night view of Earth from orbit with glowing city lights">
      <polygon points="0,0 963,0 963,665 0,808" fill="url(#night-sky)"/>
      <polygon points="0,0 963,0 963,665 0,808" fill="url(#city-glow)"/>
    </g>
    <polygon points="0,0 79,0 79,312 0,325" fill="var(--royal)"/>
    <rect x="79" y="0" width="383" height="750" fill="#0a0d18" opacity="0.35"/>

    <polygon points="79,0 462,0 462,226 79,283" fill="var(--white)"/>
    <polygon points="71,281 471,222 471,236 71,295" fill="url(#orange-bar)"/>
    <polygon points="463,250 743,207 743,221 463,264" fill="url(#orange-bar)"/>

    <polygon points="0,808 963,665 963,1340 0,1340" fill="var(--white)"/>
    <polygon points="87,786 462,731 462,744 87,799" fill="url(#blue-bar)"/>
    <polygon points="683,727 963,685 963,697 683,739" fill="var(--royal)"/>
    <polygon points="838,757 963,738 963,790 838,810" fill="url(#orange-bar)"/>
    <polygon points="0,855 122,836 122,886 0,905" fill="url(#orange-bar)"/>

    <rect x="0" y="1140" width="963" height="14" fill="var(--orange)"/>
    <rect x="0" y="1154" width="963" height="186" fill="url(#footer-band)"/>
  </svg>

  <div class="abs brand-box">
    <div class="brand-name">norvane</div>
    <div class="brand-tagline">Internet-Telephone-Security-Networking</div>
  </div>

  <ul class="abs contact">
    <li><svg viewBox="0 0 24 24"><path fill="#fff" d="M6.6 10.8a15.1 15.1 0 0 0 6.6 6.6l2.2-2.2c.3-.3.7-.4 1-.2 1.1.4 2.3.6 3.6.6.6 0 1 .4 1 1V20c0 .6-.4 1-1 1A17 17 0 0 1 3 4c0-.6.4-1 1-1h3.5c.6 0 1 .4 1 1 0 1.3.2 2.5.6 3.6.1.3 0 .7-.2 1z"/></svg>555.014.2290</li>
    <li><svg viewBox="0 0 24 24"><rect x="2.5" y="5" width="19" height="14" fill="none" stroke="#fff" stroke-width="1.6"/><path d="M2.5 5l9.5 8 9.5-8M2.5 19l7-6.5M21.5 19l-7-6.5" fill="none" stroke="#fff" stroke-width="1.6"/></svg>sales@norvanetech.com</li>
    <li><svg viewBox="0 0 24 24"><g fill="none" stroke="#fff" stroke-width="1.4"><circle cx="12" cy="12" r="9"/><ellipse cx="12" cy="12" rx="4" ry="9"/><path d="M3 12h18M4.5 7.5h15M4.5 16.5h15"/></g></svg>www.norvanetech.com</li>
  </ul>

  <div class="abs hero hero-phone">PHONE</div>
  <div class="abs hero hero-services">SERVICES</div>
  <div class="abs hero hero-price">$19.95/</div>
  <div class="abs hero hero-period">MONTH</div>
  <svg class="abs hero-icon" viewBox="0 0 82 80" aria-label="Telephone icon">
    <path fill="#fff" d="M4 18c0-8 16-14 37-14s37 6 37 14v5c0 2-2 3-4 3H60c-2 0-3-1-3-3v-4c-5-1-10-1-16-1s-11 0-16 1v4c0 2-1 3-3 3H8c-2 0-4-1-4-3z"/>
    <path fill="#fff" d="M20 28h42l12 38c1 5-2 10-7 10H15c-5 0-8-5-7-10z"/>
    <circle cx="41" cy="55" r="12" fill="#0d1430"/>
    <circle cx="41" cy="55" r="7" fill="#fff"/>
    <circle cx="41" cy="55" r="3" fill="#0d1430"/>
  </svg>

  <h2 class="abs fiber-title">HIGH SPEED<br>FIBER INTERNET</h2>
  <h3 class="abs sub-head bandwidth-head">Bandwidth Options:</h3>
  <ul class="abs bullets bandwidth-list">
    <li>100Mbps starting at $135/mo</li>
    <li>150Mbps starting at $185/mo</li>
    <li>*Price varies depending on location</li>
  </ul>
  <p class="abs fiber-notes">Features/Benefits: Dedicated symmetrical uplink &amp; downlink speeds, no slow down during peak times, 99.99% uptime guarantee, static IP address, local support.</p>

  <div class="abs column-rule"></div>

  <h3 class="abs phone-col sub-head opts-head">Telephone Options :</h3>
  <ul class="abs phone-col bullets opts-list">
    <li>Voxa V23 with three-way audio calling, 2.8" Black &amp; White LCD Display, 3 programmable keys, wired headset support, etc.</li>
    <li>Voxa V29 with three-way audio calling, 4.3" Color LCD Display, 10 programmable keys, wireless headset support, etc.</li>
  </ul>
  <h3 class="abs phone-col sub-head pricing-head">Telephone Pricing Options:</h3>
  <ul class="abs phone-col bullets pricing-list">
    <li>Voxa V23 purchase for $75 each or monthly rental of $2.00/mo</li>
    <li>Voxa V29 purchase for $135 each or monthly rental of $3.50/mo</li>
  </ul>
  <h3 class="abs phone-col sub-head features-head">Business Telephone Features:</h3>
  <p class="abs phone-col features-text">Caller-ID, Call Forwarding, Call Transfer, Virtual Assistance/Auto Attendant, Simultaneous Ring, Mobile App,1-line per phone included, 1 telephone number per phone included and much more. For more information head to www.norvanetech.com.</p>

  <h2 class="abs services-title">IT Services</h2>
  <ul class="abs service-list svc-1">
    <li>PC Protection</li>
    <li>Server Protection</li>
    <li>Backups &amp; Disaster Recovery</li>
    <li>Email/Spam Protection</li>
  </ul>
  <ul class="abs service-list svc-2">
    <li>PC &amp; Network Hardware Sales</li>
    <li>Software Sales</li>
    <li>Consulting</li>
    <li>Cloud Services</li>
  </ul>
  <ul class="abs service-list svc-3">
    <li>Ransomware Protection</li>
    <li>Cloud Office Suite</li>
    <li>Troubleshooting/Repair</li>
    <li>WiFi</li>
  </ul>
  <p class="abs rate-note">*Standard hourly rate $75/hr or customized monthly rate for all services</p>
</main>
</body>
</html>
```